New Brand - Website Design (4 Pages)

We are launching a new brand for electronic cigarettes. We already have logo and packaging done and would like a web design to go with it.

We are interested in the following deliverables:

1) Home Page Design
2) Check Out Design
3) How it Works Page
4) Secondary Template Page Design

Looking for a 60s modern look and something that is consistent with our logo and packaging.

Industry/Entity Type

Electronic

Requirements
Must have
• Consistent with logo and packaging (Use Logo Attached)
White background

Example (Functionality & Design): http://www.brolvap.co.uk/
Example (Design): http://www.plumtorva.com/

We want the design more like plumtorva but the functionality the same as brolvap.

Top Bar: Pella Marks Kits; Cartridge Refills; How it Works; Contact; My Account; Checkout
Should not have
• Stock List or Search Bar or Newsletter Signup

```html
<!DOCTYPE html>
<html lang="en">
<head>
<meta charset="utf-8">
<title>Pella Marks — Home</title>
<link rel="stylesheet" href="https://fonts.googleapis.com/css2?family=Josefin+Sans:wght@100;300;700&family=Yanone+Kaffeesatz:wght@300;400;500&display=swap">
<style>
:root{
  --sky:#8fd4f6;
  --sky-deep:#1d8fcf;
  --ink:#111111;
  --paper:#ffffff;
  --band:#c6c6c6;
  --text:#2b2b2b;
  --rule:#6e6e6e;
  --accent:#c9533f;
  --apple:#c9533f;
  --banana:#eec90a;
  --tobacco:#553409;
  --menthol:#6aa114;
  --plain:#a8a8a8;
  --footer:#404040;
  --pack-dark:#262626;
  --pack-red:#c54f3b;
}
*{margin:0;padding:0;box-sizing:border-box}
html,body{width:903px;height:1200px;overflow:hidden;background:var(--paper)}
body{position:relative;font-family:"Yanone Kaffeesatz",sans-serif;color:var(--text)}
.abs{position:absolute}

.brand-dot{left:71px;top:24px;width:88px;height:88px;border-radius:50%;background:var(--sky);z-index:3}
.brand-name{left:169px;top:22px;font-family:"Yanone Kaffeesatz",sans-serif;font-weight:500;font-size:44px;line-height:1;color:var(--ink);letter-spacing:1px;z-index:3}
.hotline{right:65px;top:26px;text-align:right;color:var(--accent);font-weight:400;line-height:1}
.hotline .hours{font-size:20px}
.hotline .phone{font-size:26px;margin-top:10px;letter-spacing:1px}

.topnav{left:0;top:88px;width:903px;height:35px;background:var(--ink);color:var(--paper);font-size:21px;z-index:2}
.topnav ul{list-style:none;position:absolute;top:4px;display:flex}
.topnav li+li::before{content:"|";margin:0 9px;color:#bbb;font-size:16px;position:relative;top:-2px}
.nav-main{left:169px}
.nav-user{right:64px}
.cart{display:inline-block;vertical-align:middle;margin-left:6px;margin-top:-4px}

.hero{left:0;top:123px;width:903px;height:354px;background:var(--sky);overflow:hidden}
.hero-clouds{position:absolute;left:0;top:0}
.hero-copy{left:79px;top:70px;color:var(--paper);font-family:"Josefin Sans",sans-serif;line-height:1}
.hero-copy .intro{font-weight:100;font-size:42px;letter-spacing:1px}
.hero-copy .name{font-weight:700;font-size:45px;margin-top:8px;letter-spacing:.5px}
.hero-copy .flavor{font-weight:100;font-size:33px;margin-top:6px;letter-spacing:1px}
.buy{left:79px;top:246px;width:194px;height:36px;border-radius:18px;background:#222;overflow:hidden;color:var(--paper);font-family:"Josefin Sans",sans-serif;font-weight:700;font-size:20px}
.buy .tip{position:absolute;left:0;top:0;width:52px;height:36px;background:#f4f4f4;border-radius:18px 0 0 18px}
.buy .label{position:absolute;left:68px;top:10px;letter-spacing:1px}
.product{left:513px;top:19px;width:223px;height:240px;border-radius:4px;background:linear-gradient(180deg,var(--pack-dark) 0%,var(--pack-dark) 62%,var(--pack-red) 100%)}
.slider-dots{left:864px;top:110px}
.slider-dots span{display:block;width:10px;height:10px;border-radius:50%;border:2px solid var(--paper);margin-bottom:36px}
.slider-dots span.on{background:var(--paper)}

.promises{left:0;top:477px;width:903px;height:32px;background:var(--band)}
.promise{top:-25px;display:flex;align-items:center;color:var(--paper);font-size:22px}
.promise .badge{width:64px;height:64px;border-radius:50%;background:var(--sky-deep);margin-right:8px;display:flex;align-items:center;justify-content:center;color:var(--paper);flex-direction:column;font-family:"Josefin Sans",sans-serif;font-weight:700;line-height:.9}
.promise .badge b{font-size:26px}
.promise .badge small{font-size:14px}
.promise .label{position:relative;top:12px}

.section-title{left:69px;width:770px;display:flex;align-items:center;font-size:22px;font-weight:400;letter-spacing:2px;color:#3b3b3b}
.section-title::before,.section-title::after{content:"";flex:1;height:1px;background:var(--rule)}
.section-title span{padding:0 12px}

.reason{top:592px}
.reason .icon{height:100px;display:flex;justify-content:center;align-items:center}
.reason h3{font-weight:400;font-size:20px;margin-top:22px;letter-spacing:.5px}
.reason p{font-weight:400;font-size:14px;line-height:17.5px;text-align:justify;margin-top:2px}

.flavour{top:886px;width:160px;text-align:center;font-size:22px;line-height:1}
.flavour svg{display:block;margin:0 auto 10px}

.site-footer{left:0;top:1132px;width:903px;height:68px;background:var(--footer);color:var(--paper);font-family:Arial,Helvetica,sans-serif;font-size:12px;text-align:center;padding-top:21px}
</style>
</head>
<body>

<header>
  <div class="abs brand-dot"></div>
  <div class="abs brand-name">PELLA MARKS</div>
  <div class="abs hotline">
    <div class="hours">Call FREE Mon-Fri 8am-8pm</div>
    <div class="phone">0800 XXXX XXX</div>
  </div>
  <nav class="abs topnav">
    <ul class="nav-main"><li>Pella Marks Kits</li><li>Cartridge Refills</li><li>How it Works</li></ul>
    <ul class="nav-user"><li>Contact</li><li>My Account</li><li>Checkout
      <svg class="cart" width="20" height="16" viewBox="0 0 20 16"><path d="M1 2h3l3 9h9l2-7H6" fill="none" stroke="#fff" stroke-width="2"/><circle cx="8" cy="14" r="1.6" fill="#fff"/><circle cx="15" cy="14" r="1.6" fill="#fff"/></svg></li></ul>
  </nav>
</header>

<section class="abs hero">
  <svg class="hero-clouds" width="903" height="354">
    <g fill="#ffffff" opacity=".55">
      <circle cx="760" cy="-20" r="110"/>
      <circle cx="640" cy="130" r="215"/>
      <circle cx="600" cy="300" r="90"/>
      <circle cx="735" cy="270" r="100"/>
    </g>
    <g fill="#ffffff" opacity=".8">
      <circle cx="660" cy="320" r="70"/>
      <circle cx="560" cy="250" r="80"/>
    </g>
  </svg>
  <div class="abs hero-copy">
    <div class="intro">INTRODUCING</div>
    <div class="name">PELLA MARKS</div>
    <div class="flavor">APPLE FLAVORED</div>
  </div>
  <div class="abs buy"><span class="tip"></span><span class="label">BUY NOW</span></div>
  <div class="abs product" role="img" aria-label="Product photo: apple flavoured cartomiser pack"></div>
  <div class="abs slider-dots"><span class="on"></span><span></span><span></span><span></span></div>
</section>

<section class="abs promises">
  <div class="abs promise" style="left:86px"><div class="badge"><b>30</b><small>DAY</small></div><span class="label">MONEY BACK PROMISE*</span></div>
  <div class="abs promise" style="left:352px"><div class="badge">
    <svg width="30" height="30" viewBox="0 0 30 30"><polygon points="15,3 27,9 15,15 3,9" fill="#fff"/><polygon points="3,11 14,17 14,28 3,22" fill="#fff"/><polygon points="16,17 27,11 27,22 16,28" fill="#fff"/></svg>
  </div><span class="label">FREE SHIPPING</span></div>
  <div class="abs promise" style="left:599px"><div class="badge">
    <svg width="30" height="34" viewBox="0 0 30 34"><path d="M9 18l-4 14 6-3 3 5 2-12zM21 18l4 14-6-3-3 5-2-12z" fill="#fff"/><circle cx="15" cy="13" r="10" fill="#fff"/><text x="15" y="17" text-anchor="middle" font-family="Arial" font-weight="700" font-size="11" fill="#1d8fcf">1</text></svg>
  </div><span class="label">ONE YEAR WARRANTY*</span></div>
</section>

<h2 class="abs section-title" style="top:553px"><span>WHY PELLA MARKS?</span></h2>

<article class="abs reason" style="left:72px;width:255px">
  <div class="icon"><svg width="112" height="96" viewBox="0 0 112 96" role="img" aria-label="Piggy bank savings icon">
    <ellipse cx="60" cy="52" rx="44" ry="32" fill="#8fd4f6"/><rect x="28" y="70" width="14" height="24" rx="3" fill="#8fd4f6"/><rect x="72" y="70" width="14" height="24" rx="3" fill="#8fd4f6"/><rect x="6" y="42" width="16" height="18" rx="4" fill="#8fd4f6"/><circle cx="40" cy="20" r="10" fill="#8fd4f6"/></svg></div>
  <h3>KOGTKOFOKF KFOKROGK</h3>
  <p>Phasel lus imperdiet suscipit purus nec consectetur. Vestib ulum mole stie quam lorem, a dign issim orci conseq at ac. Curabitur facilisis tempu de gyhs magna nec pretium.</p>
</article>
<article class="abs reason" style="left:340px;width:220px">
  <div class="icon"><svg width="92" height="80" viewBox="0 0 92 80"><path d="M46 78L8 40C-4 28 2 4 24 4c10 0 18 6 22 14C50 10 58 4 68 4c22 0 28 24 16 36z" fill="#8fd4f6"/></svg></div>
  <h3>NUNC EU CONSEQUAT</h3>
  <p>Fusce sodales euismod urna a placerat. Sed diam eros, dignissim a elementum ac, condim entum impe rdiet arcu. Nunc eu consequat nibh. Pellentesque non sem placerat, sodales purus sit amet.</p>
</article>
<article class="abs reason" style="left:616px;width:220px">
  <div class="icon"><svg width="70" height="104" viewBox="0 0 70 104">
    <circle cx="36" cy="6" r="4" fill="#8fd4f6"/><circle cx="27" cy="14" r="3" fill="#8fd4f6"/>
    <path d="M25 24h20v26l20 40c2 5-1 10-6 10H11c-5 0-8-5-6-10l20-40z" fill="none" stroke="#8fd4f6" stroke-width="4"/>
    <path d="M14 68h42l8 20c1 4-1 8-5 8H11c-4 0-6-4-5-8z" fill="#8fd4f6"/></svg></div>
  <h3>ABUIGIJ FKFIDK LOGKITKD</h3>
  <p>Quisque sapien magna, vulputate vel justo nec, ornare dictum augue. Morbi et ligula fringilla, dignissim dolor non, imperdiet nulla. Donec interdum turpis at bibendum feugiat. Sed dui ipsum, vestibulum vitae placerat nec.</p>
</article>

<h2 class="abs section-title" style="top:846px"><span>OUR FLAVOURS</span></h2>

<div class="abs flavour" style="left:55px;color:var(--apple)">
  <svg width="112" height="150" viewBox="0 0 112 150" role="img" aria-label="Apple flavour emblem"><circle cx="56" cy="54" r="54" fill="#c9533f"/><circle cx="56" cy="118" r="15" fill="#c9533f" stroke="#fff" stroke-width="3"/><circle cx="75" cy="126" r="12" fill="#c9533f" stroke="#fff" stroke-width="3"/><circle cx="62" cy="140" r="8" fill="#c9533f" stroke="#fff" stroke-width="3"/></svg>APPLE</div>
<div class="abs flavour" style="left:217px;color:var(--banana)">
  <svg width="112" height="150" viewBox="0 0 112 150" role="img" aria-label="Banana flavour emblem"><circle cx="56" cy="54" r="54" fill="#eec90a"/><circle cx="56" cy="118" r="15" fill="#eec90a" stroke="#fff" stroke-width="3"/><circle cx="75" cy="126" r="12" fill="#eec90a" stroke="#fff" stroke-width="3"/><circle cx="62" cy="140" r="8" fill="#eec90a" stroke="#fff" stroke-width="3"/></svg>BANANA</div>
<div class="abs flavour" style="left:379px;color:var(--tobacco)">
  <svg width="112" height="150" viewBox="0 0 112 150" role="img" aria-label="Classic tobacco flavour emblem"><circle cx="56" cy="54" r="54" fill="#553409"/><circle cx="56" cy="118" r="15" fill="#553409" stroke="#fff" stroke-width="3"/><circle cx="75" cy="126" r="12" fill="#553409" stroke="#fff" stroke-width="3"/><circle cx="62" cy="140" r="8" fill="#553409" stroke="#fff" stroke-width="3"/></svg>CLASSIC TOBACCO</div>
<div class="abs flavour" style="left:542px;color:var(--menthol)">
  <svg width="112" height="150" viewBox="0 0 112 150" role="img" aria-label="Menthol flavour emblem"><circle cx="56" cy="54" r="54" fill="#6aa114"/><circle cx="56" cy="118" r="15" fill="#6aa114" stroke="#fff" stroke-width="3"/><circle cx="75" cy="126" r="12" fill="#6aa114" stroke="#fff" stroke-width="3"/><circle cx="62" cy="140" r="8" fill="#6aa114" stroke="#fff" stroke-width="3"/></svg>MENTHOL</div>
<div class="abs flavour" style="left:693px;color:var(--plain)">
  <svg width="112" height="150" viewBox="0 0 112 150" role="img" aria-label="Non-nicotine tobacco flavour emblem"><circle cx="56" cy="54" r="54" fill="#a8a8a8"/><circle cx="56" cy="118" r="15" fill="#a8a8a8" stroke="#fff" stroke-width="3"/><circle cx="75" cy="126" r="12" fill="#a8a8a8" stroke="#fff" stroke-width="3"/><circle cx="62" cy="140" r="8" fill="#a8a8a8" stroke="#fff" stroke-width="3"/></svg>NON-NICOTINE<br>TOBACCO</div>

<footer class="abs site-footer">Copyright 2013 Pella Marks - Terms &amp; Conditions | Privacy Policy</footer>

</body>
</html>
```